Lumenvale Consulting Group

This is a new consulting business in the area of broadband technology. The logo should reflect the key aspects of our expertise - fiber optic networking and wireless high speed data.

Target Market(s)

Multi unit housing. hotel and subdivision developers, city communications authorities, ISP's

Industry/Entity Type

Telecommunications

Contact Information for Business Card

A logo that reflects the type of business

Font styles to use
Sans Serif

Colors

Designer to choose colors to be used in the design.

Requirements
Must have
• Logo, name, job title, contact info including address, cellphone number, email address and web URL (www.lumenvaleconsultinggroup.com)

```html
<!DOCTYPE html>
<html lang="en">
<head>
<meta charset="utf-8">
<title>Lumenvale Consulting Group – Business Card</title>
<link href="https://fonts.googleapis.com/css2?family=Montserrat:wght@400;500;700&display=swap" rel="stylesheet">
<style>
  :root {
    --backdrop: #26272a;
    --brand-red: #d92f33;
    --brand-red-deep: #b8252a;
    --ink: #3a3b3e;
    --ink-soft: #5b5c60;
    --paper: #f7f7f7;
    --white: #ffffff;
    --rule: #8e8f93;
  }
  * { margin: 0; padding: 0; box-sizing: border-box; }
  html, body { width: 1200px; height: 660px; overflow: hidden; }
  body {
    background: var(--backdrop);
    font-family: "Montserrat", Arial, sans-serif;
    position: relative;
  }
  .card {
    position: absolute;
    top: 175px;
    width: 540px;
    height: 310px;
    border-radius: 3px;
    overflow: hidden;
    box-shadow: 0 14px 30px rgba(0,0,0,.45);
  }
  /* Front */
  .card--front {
    left: 40px;
    background: linear-gradient(135deg, var(--brand-red) 0%, var(--brand-red-deep) 100%);
    display: flex;
    align-items: center;
    justify-content: center;
  }
  .wordmark {
    display: flex;
    align-items: center;
    gap: 14px;
  }
  .wordmark__dot {
    width: 22px; height: 22px; border-radius: 50%;
    background: var(--white);
    flex: none;
  }
  .wordmark__name {
    color: var(--white);
    font-weight: 700;
    font-size: 24px;
    line-height: 1.12;
  }
  /* Back */
  .card--back {
    left: 620px;
    background: var(--paper);
  }
  .card__shapes { position: absolute; inset: 0; }
  .back__logo {
    position: absolute;
    left: 34px; top: 62px;
    gap: 10px;
  }
  .back__logo .wordmark__dot { background: var(--brand-red); width: 16px; height: 16px; }
  .back__logo .wordmark__name { color: var(--brand-red); font-size: 19px; }
  .holder {
    position: absolute;
    right: 32px; top: 40px;
    text-align: right;
  }
  .holder__name {
    font-size: 18px;
    font-weight: 500;
    color: var(--ink);
    letter-spacing: .5px;
  }
  .holder__title {
    font-size: 13px;
    color: var(--brand-red);
    margin-top: 1px;
  }
  .contacts {
    position: absolute;
    left: 30px; top: 206px;
    list-style: none;
  }
  .contacts li {
    display: flex;
    align-items: center;
    gap: 9px;
    font-size: 12.5px;
    font-weight: 500;
    color: var(--ink);
    height: 20px;
  }
  .contacts svg { width: 13px; height: 13px; flex: none; }
</style>
</head>
<body>

  <section class="card card--front" aria-label="Card front">
    <div class="wordmark">
      <span class="wordmark__dot"></span>
      <span class="wordmark__name">Lumenvale<br>Consulting Group</span>
    </div>
  </section>

  <section class="card card--back" aria-label="Card back">
    <svg class="card__shapes" viewBox="0 0 540 310" aria-hidden="true">
      <line x1="300" y1="90" x2="515" y2="90" stroke="var(--rule)" stroke-width="1"/>
      <circle cx="488" cy="100" r="4" fill="var(--brand-red)"/>
      <line x1="24" y1="198" x2="250" y2="198" stroke="var(--rule)" stroke-width="1"/>
      <polygon points="300,310 540,228 540,310" fill="var(--brand-red)"/>
      <polygon points="330,310 540,246 540,310" fill="var(--paper)"/>
      <path d="M420 210 Q420 196 434 196 L540 196 L540 228 L420 228 Z" fill="var(--ink)"/>
    </svg>

    <div class="wordmark back__logo">
      <span class="wordmark__dot"></span>
      <span class="wordmark__name">Lumenvale<br>Consulting Group</span>
    </div>

    <div class="holder">
      <div class="holder__name">ALEX MORGAN</div>
      <div class="holder__title">president</div>
    </div>

    <ul class="contacts">
      <li>
        <svg viewBox="0 0 14 14"><rect x="3" y="1" width="8" height="12" rx="1.5" fill="none" stroke="var(--brand-red)" stroke-width="1.6"/><circle cx="7" cy="10.5" r=".9" fill="var(--brand-red)"/></svg>
        01632 960481
      </li>
      <li>
        <svg viewBox="0 0 14 14"><path d="M2 5 Q7 1 12 5 L10.5 6.5 L9 5.5 L5 5.5 L3.5 6.5 Z" fill="var(--brand-red)"/><rect x="3" y="7" width="8" height="5" rx="1" fill="var(--brand-red)"/></svg>
        01632 960482
      </li>
      <li>
        <svg viewBox="0 0 14 14"><rect x="1" y="3" width="12" height="8" fill="var(--brand-red)"/><path d="M1 3 L7 8 L13 3" fill="none" stroke="var(--white)" stroke-width="1.1"/></svg>
        alex@lumenvale.com
      </li>
      <li>
        <svg viewBox="0 0 14 14"><circle cx="7" cy="7" r="5.5" fill="none" stroke="var(--brand-red)" stroke-width="1.4"/><ellipse cx="7" cy="7" rx="2.3" ry="5.5" fill="none" stroke="var(--brand-red)" stroke-width="1.1"/><line x1="1.5" y1="7" x2="12.5" y2="7" stroke="var(--brand-red)" stroke-width="1.1"/></svg>
        www.lumenvaleconsultinggroup.com
      </li>
    </ul>
  </section>

</body>
</html>
```